UK garage/funky house night flier

I need a flier design to upload to my facebook event page and also some printed fliers to promote the event.

Event is in an urban area underneath railway arches so would like a flier to reflect this with an urban background.
Updates

new photos uploaded to be used as possible backgrounds

Target Market(s)

aged 18-30

Industry/Entity Type

House

Requirements
Must have
• The following text on front of flier:

MIDNIGHT KREST PROMOTIONS PRESENTS A NIGHT CALLED…

‘COPPER TUNNEL RHYTHMZ’

Saturday 7th September 2013

@ Dock27, Marlow Lane, Digbeth, Birmingham B7 3QX

9pm till late

DJ’s playing a selection of Funky house/deep house/future garage and old school 2-step garage

(On back of flier......)

Come and enjoy yourself in a friendly, safe environment with like-minded people who are out to have a good time and rave till the early hours. This venue is part outdoor terrace and part indoor with music being played on the Sonorix-Max Soundsystem – so you know it is a night not to be missed!!

This event is guestlist only. Those not on the guest list will not be allowed entry. To get yourself on the guest list go to the facebook page www.socialpagehub.example/midnightkrestpromotions and join the event ‘Copper Tunnel Rhythmz’

Dresscode: smart. No trainers/tracksuits
Admission fee on the door is £5
Last entry: midnight
Nice to have
• must be portrait, A5 or A6 size

Urban background, maybe at night, a street with old brickwork, maybe some speakers in the foreground.

dock27 logo bottom right

Back of flier to have the map of Dock27

```html
<!DOCTYPE html>
<html lang="en">
<head>
<meta charset="utf-8">
<title>Copper Tunnel Rhythmz</title>
<link rel="stylesheet" href="https://fonts.googleapis.com/css2?family=Arvo:wght@700&family=Bebas+Neue&family=Lobster+Two:ital,wght@0,400;0,700&family=Yellowtail&display=swap">
<style>
  :root {
    --ink: #ffffff;
    --night: #0e0d10;
    --brick: #3a373b;
    --brick-deep: #242226;
    --stone: #8a8790;
    --haze: #dcd9df;
    --violet: #7b4a9a;
    --violet-deep: #4e2f66;
    --violet-soft: #b49cc7;
  }
  html, body {
    margin: 0;
    padding: 0;
    overflow: hidden;
    background: var(--night);
  }
  .flier {
    position: relative;
    width: 846px;
    height: 1200px;
    overflow: hidden;
    background: var(--night);
    color: var(--ink);
  }
  .backdrop,
  .facets,
  .shade {
    position: absolute;
    inset: 0;
    width: 846px;
    height: 1200px;
  }
  .shade {
    background: linear-gradient(180deg, rgba(14,13,16,0) 0%, rgba(14,13,16,0) 55%, rgba(14,13,16,0.75) 75%, rgba(14,13,16,0.95) 100%);
  }
  .presenter {
    position: absolute;
    top: 28px;
    left: 808px;
    margin: 0;
    transform-origin: 0 0;
    transform: rotate(90deg);
    white-space: nowrap;
    font-family: "Bebas Neue", sans-serif;
    font-size: 19px;
    letter-spacing: 1.6px;
    line-height: 1;
  }
  .event-info {
    position: absolute;
    right: 48px;
    top: 676px;
    text-align: right;
  }
  .title {
    margin: 0;
    font-weight: normal;
  }
  .title-script {
    display: block;
    font-family: "Yellowtail", "Lobster Two", cursive;
    font-size: 96px;
    line-height: 1;
    margin-right: 4px;
  }
  .title-outline {
    display: block;
    font-family: "Arvo", serif;
    font-weight: 700;
    font-size: 82px;
    line-height: 1;
    margin-top: 2px;
    letter-spacing: 8px;
    margin-right: -8px;
    color: transparent;
    -webkit-text-stroke: 2px var(--ink);
  }
  .title-solid {
    display: block;
    font-family: "Arvo", serif;
    font-weight: 700;
    font-size: 98px;
    line-height: 1;
    margin-top: 0;
    letter-spacing: 8px;
    margin-right: -8px;
  }
  .date {
    margin: 22px 0 0;
    font-family: "Bebas Neue", sans-serif;
    font-size: 46px;
    line-height: 1;
    letter-spacing: 1.5px;
  }
  .venue {
    margin: 12px 0 0;
    font-family: "Bebas Neue", sans-serif;
    font-size: 26px;
    line-height: 1;
    letter-spacing: 2.4px;
  }
  .lineup {
    margin: 22px 0 0;
    font-family: "Bebas Neue", sans-serif;
    font-size: 22px;
    line-height: 1.15;
    letter-spacing: 1px;
  }
</style>
</head>
<body>
  <main class="flier">
    <svg class="backdrop" viewBox="0 0 846 1200" role="img" aria-label="Black and white photograph of a brick railway arch passageway with a corrugated fence on the left and graffiti, tinted purple">
      <defs>
        <linearGradient id="wall" x1="0" y1="0" x2="1" y2="0">
          <stop offset="0" stop-color="#e4e2e6"/>
          <stop offset="0.2" stop-color="#9a979e"/>
          <stop offset="0.26" stop-color="#4a474d"/>
          <stop offset="0.6" stop-color="#5a575d"/>
          <stop offset="1" stop-color="#2a282c"/>
        </linearGradient>
        <radialGradient id="tunnel" cx="0.5" cy="0.5" r="0.5">
          <stop offset="0" stop-color="#d8cbe2"/>
          <stop offset="0.45" stop-color="#8d65a8"/>
          <stop offset="1" stop-color="#8d65a8" stop-opacity="0"/>
        </radialGradient>
        <linearGradient id="floor" x1="0" y1="0" x2="0" y2="1">
          <stop offset="0" stop-color="#555258" stop-opacity="0"/>
          <stop offset="1" stop-color="#1a191c"/>
        </linearGradient>
      </defs>
      <rect width="846" height="1200" fill="url(#wall)"/>
      <rect x="0" y="0" width="846" height="200" fill="var(--brick)" opacity="0.55"/>
      <ellipse cx="320" cy="560" rx="200" ry="260" fill="url(#tunnel)"/>
      <rect x="0" y="700" width="846" height="500" fill="url(#floor)"/>
    </svg>

    <svg class="facets" viewBox="0 0 846 1200" aria-hidden="true">
      <polygon points="560,250 846,60 846,270 610,420" fill="var(--violet)" opacity="0.6"/>
      <polygon points="610,420 846,270 846,560" fill="var(--brick-deep)" opacity="0.75"/>
      <polygon points="470,360 600,300 640,420" fill="var(--violet)" opacity="0.45"/>
      <polygon points="0,420 180,360 180,700 0,760" fill="var(--violet)" opacity="0.55"/>
      <polygon points="0,760 180,700 180,880 0,920" fill="var(--violet-deep)" opacity="0.6"/>
      <rect x="200" y="220" width="140" height="30" fill="var(--stone)" opacity="0.5"/>
      <rect x="230" y="300" width="190" height="40" fill="var(--violet)" opacity="0.55"/>
      <rect x="180" y="400" width="150" height="36" fill="var(--haze)" opacity="0.35"/>
      <rect x="420" y="400" width="180" height="50" fill="var(--violet-deep)" opacity="0.5"/>
      <rect x="440" y="560" width="240" height="40" fill="var(--brick-deep)" opacity="0.55"/>
      <rect x="300" y="500" width="130" height="30" fill="var(--violet-soft)" opacity="0.4"/>
      <polygon points="425,255 445,230 465,255" fill="var(--haze)" opacity="0.7"/>
      <polygon points="280,300 330,330 280,360" fill="var(--brick-deep)" opacity="0.6"/>
      <polygon points="400,470 450,500 400,530" fill="var(--haze)" opacity="0.45"/>
      <polygon points="520,480 570,400 600,480" fill="var(--violet-deep)" opacity="0.6"/>
      <polygon points="180,620 260,680 180,740" fill="var(--haze)" opacity="0.3"/>
      <polygon points="200,760 330,640 330,760" fill="var(--violet)" opacity="0.45"/>
    </svg>

    <div class="shade"></div>

    <p class="presenter">MIDNIGHT KREST PROMOTIONS PRESENTS</p>

    <section class="event-info">
      <h1 class="title">
        <span class="title-script">Copper</span>
        <span class="title-outline">TUNNEL</span>
        <span class="title-solid">RHYTHMZ</span>
      </h1>
      <p class="date">SATURDAY 7TH SEPTEMBER 2013</p>
      <p class="venue">@ DOCK27, MARLOW LANE, DIGBETH, BIRMINGHAM B7 3QX</p>
      <p class="lineup">DJs PLAYING A SELECTION OF FUNKY HOUSE/DEEP HOUSE/FUTURE GARAGE<br>AND OLD SCHOOL 2-STEP GARAGE &nbsp;/ &nbsp;9PM TIL LATE</p>
    </section>
  </main>
</body>
</html>
```